Email Signature

We want a new email signature designed that will include an employees picture and our logo at minimum. Of course contact info as well.

For the sample please create the new signature for Dale Prentiss...extra pics provided
please visit our website www.BrovaneServicing.example

Need to limit links to our website....government email servers strip out many.
Updates

I have a new draft design I'd like to work from...simple and clean.Needs:LogoDisclaimerand a bit of colorI'd like to make selection this week. Added Tuesday, October 24, 2017

Target Market(s)

other professional businesses

Requirements
Must have
• picture & Logo
• new look and something that auto scales to the emails window.
• Would like to have a new tag line "

```html
<!DOCTYPE html>
<html lang="en">
<head>
<meta charset="utf-8">
<title>Email Signature – Dale Prentiss</title>
<link rel="stylesheet" href="https://fonts.googleapis.com/css2?family=Montserrat:wght@400;500;600;700&display=swap">
<style>
  :root {
    --brand-blue: #1f4394;
    --brand-red: #e3231b;
    --white: #ffffff;
    --fine-grey: #a9a9ab;
    --photo-dark: #2b2f3a;
    --photo-light: #e9e7e4;
  }
  * { margin: 0; padding: 0; box-sizing: border-box; }
  html, body { width: 1200px; height: 388px; overflow: hidden; background: var(--white); }
  .signature {
    position: relative;
    width: 1200px;
    height: 388px;
    font-family: "Montserrat", Arial, sans-serif;
    background: var(--white);
  }
  .signature__band {
    position: absolute; left: 0; top: 0;
    width: 1200px; height: 258px;
    background: var(--brand-blue);
  }
  .portrait__accent {
    position: absolute; left: 45px; top: 135px;
    width: 198px; height: 210px;
    background: var(--brand-red);
  }
  .portrait {
    position: absolute; left: 54px; top: 45px;
    width: 243px; height: 293px;
    background: linear-gradient(180deg, var(--photo-light) 0%, var(--photo-light) 38%, #8a8c92 62%, var(--photo-dark) 100%);
  }
  .contact {
    position: absolute; left: 348px; top: 66px;
    color: var(--white);
  }
  .contact__name {
    font-size: 33px; font-weight: 500; letter-spacing: 0.2px; line-height: 1;
  }
  .contact__title {
    margin-top: 12px;
    font-size: 16px; font-weight: 500; color: var(--brand-red);
  }
  .contact__details {
    margin-top: 36px;
    font-size: 14.5px; font-weight: 600; line-height: 26px;
  }
  .contact__details .sep { padding: 0 10px; font-weight: 400; }
  .company-name {
    position: absolute; left: 930px; top: 48px; width: 230px;
    text-align: center;
    color: var(--white);
    font-size: 25px; font-weight: 700; line-height: 29px; text-transform: uppercase;
  }
  .social {
    position: absolute; left: 948px; top: 196px;
    display: flex; gap: 16px;
  }
  .social__dot {
    width: 37px; height: 37px; border-radius: 50%;
    background: var(--brand-red);
    border: 2px solid var(--white);
  }
  .disclaimer {
    position: absolute; left: 345px; top: 278px; width: 840px;
    font-size: 9.3px; line-height: 11.4px; font-weight: 400;
    color: var(--fine-grey); text-align: justify;
  }
</style>
</head>
<body>
<div class="signature">
  <div class="signature__band"></div>

  <div class="portrait__accent"></div>
  <div class="portrait" role="img" aria-label="Portrait photo of Dale Prentiss in a dark suit with arms crossed"></div>

  <div class="contact">
    <h1 class="contact__name">Dale Prentiss</h1>
    <p class="contact__title">Director of Pre-Construction</p>
    <div class="contact__details">
      <p>418 Calder Street Suite B, Harlow Point, Maryland 21555</p>
      <p>DPrentiss@BrovaneServicing.example<span class="sep">|</span>www.BrovaneServicing.example</p>
      <p>C. 410-555-0161<span class="sep">|</span>O. 800-555-0173 x206<span class="sep">|</span>F. 800-555-0174</p>
    </div>
  </div>

  <div class="company-name">Brovane<br>Servicing<br>Incorporated</div>

  <div class="social" aria-label="Social profiles">
    <span class="social__dot"></span>
    <span class="social__dot"></span>
    <span class="social__dot"></span>
    <span class="social__dot"></span>
  </div>

  <p class="disclaimer">This Email message and any attachment may contain information that is proprietary, legally privileged, confidential, and/or subject to copyright belonging to Brovane Servicing Inc ("BSI"). This Email is intended solely for the use of the person(s) to which it is addressed and is not subject to FOIA. If you are not an intended recipient, or the employee or agent responsible for delivery of this Email to the intended recipient(s), you are hereby notified that any dissemination, distribution or copying of this Email is strictly prohibited.... If you have received this message in error, please immediately notify the sender and permanently delete this Email and any copies. BSI policies expressly prohibit employees from making defamatory or offensive statements and infringing any copyright or any other legal right by Email communication. BSI will not accept any liability in respect of such communications.</p>
</div>
</body>
</html>
```